Quellora business card design

create modern and tech looking business card that is clean but effectively communciates that we are a cloud communications company.
Should have at minimum:
Employee Name
Postion
Phone Number
Email
website
Contact Information for Business Card
create modern and tech looking business card that is clean but effectively communciates that we are a cloud communications company. We have two logo color schemes (attached) so would like to see designs both ways
Should have at minimum:
Employee Name
Postion
Phone Number
Email
website

```html
<!DOCTYPE html>
<html lang="en">
<head>
<meta charset="utf-8">
<title>Quellora business card</title>
<link rel="stylesheet" href="https://fonts.googleapis.com/css2?family=Open+Sans:wght@400;600&display=swap">
<style>
  :root {
    --backdrop: #cfd0d2;
    --card: #13161b;
    --lime: #9ccb3f;
    --sky: #2bc1e6;
    --wordmark: #8b8f95;
    --ink: #f2f3f5;
  }
  * { box-sizing: border-box; margin: 0; padding: 0; }
  html, body {
    width: 1200px; height: 1200px; overflow: hidden;
    background: var(--backdrop);
    font-family: "Open Sans", Arial, sans-serif;
  }
  .sheet {
    position: relative; width: 1200px; height: 1200px;
    display: flex; flex-direction: column; align-items: center; justify-content: center; gap: 70px;
  }
  .card {
    position: relative; width: 860px; height: 491px;
    background: var(--card); overflow: hidden;
    box-shadow: 0 6px 18px rgba(0,0,0,0.25);
  }
  .graphic-area { position: absolute; }
  .card-front .graphic-area {
    left: 0; top: 0; width: 460px; height: 491px;
    background: linear-gradient(150deg, var(--lime) 0%, rgba(156,203,63,0.75) 30%, rgba(43,193,230,0.55) 60%, rgba(19,22,27,0) 90%);
  }
  .card-back .graphic-area {
    left: 0; top: 120px; width: 470px; height: 371px;
    background: linear-gradient(150deg, var(--lime) 0%, rgba(156,203,63,0.75) 30%, rgba(43,193,230,0.55) 60%, rgba(19,22,27,0) 90%);
  }
  .wordmark {
    position: absolute; display: flex; align-items: center; gap: 14px;
    color: var(--wordmark); font-weight: 600; letter-spacing: 3px; line-height: 1;
  }
  .wordmark-square { width: 22px; height: 22px; background: var(--lime); flex: none; }
  .card-front .wordmark { left: 470px; top: 180px; font-size: 56px; }
  .card-back .wordmark { right: 70px; top: 56px; font-size: 40px; }
  .card-back .wordmark-square { width: 16px; height: 16px; }
  .identity { position: absolute; right: 70px; top: 140px; text-align: right; color: var(--ink); }
  .identity-name { font-size: 36px; font-weight: 400; line-height: 1.1; }
  .identity-role { font-size: 17px; margin-top: 4px; }
  .contact-list {
    position: absolute; right: 70px; top: 255px; list-style: none;
    color: var(--ink); font-size: 17px; line-height: 1.3;
  }
  .contact-item { display: flex; align-items: flex-start; gap: 10px; margin-bottom: 12px; }
  .contact-icon { width: 16px; height: 16px; flex: none; margin-top: 3px; fill: var(--sky); }
</style>
</head>
<body>
<main class="sheet">

  <section class="card card-front" aria-label="Card front">
    <div class="graphic-area" role="img" aria-label="Decorative lime and blue geometric pattern"></div>
    <div class="wordmark"><span class="wordmark-square"></span>Quellora</div>
  </section>

  <section class="card card-back" aria-label="Card back">
    <div class="graphic-area" role="img" aria-label="Decorative lime and blue geometric pattern"></div>
    <div class="wordmark"><span class="wordmark-square"></span>Quellora</div>
    <div class="identity">
      <p class="identity-name">Daniel Verhoeven</p>
      <p class="identity-role">C.E.O</p>
    </div>
    <ul class="contact-list">
      <li class="contact-item">
        <svg class="contact-icon" viewBox="0 0 16 16" aria-hidden="true"><path d="M8 0a5.5 5.5 0 0 0-5.5 5.5C2.5 10 8 16 8 16s5.5-6 5.5-10.5A5.5 5.5 0 0 0 8 0zm0 8a2.5 2.5 0 1 1 0-5 2.5 2.5 0 0 1 0 5z"/></svg>
        <span>12, Harbor Lane, 3rd Floor,<br>Suite no. 21, CA</span>
      </li>
      <li class="contact-item">
        <svg class="contact-icon" viewBox="0 0 16 16" aria-hidden="true"><path d="M3.6 0.8l2.3 3.2-1.5 1.8c0.9 2 2.7 3.9 4.8 4.9l1.8-1.5 3.2 2.3-1.4 3.2C7 14.5 1.4 8.9 0.6 2.2z"/></svg>
        <span>5550142297</span>
      </li>
      <li class="contact-item">
        <svg class="contact-icon" viewBox="0 0 16 16" aria-hidden="true"><path d="M0 3h16v1.2L8 9 0 4.2zm0 2.6l8 4.8 8-4.8V13H0z"/></svg>
        <span>hello@quellora.com</span>
      </li>
      <li class="contact-item">
        <svg class="contact-icon" viewBox="0 0 16 16" aria-hidden="true"><circle cx="8" cy="8" r="7" fill="none" stroke="var(--sky)" stroke-width="1.6"/><path d="M1 8h14M8 1c-3 3.5-3 10.5 0 14M8 1c3 3.5 3 10.5 0 14" fill="none" stroke="var(--sky)" stroke-width="1.3"/></svg>
        <span>www.quellora.com</span>
      </li>
    </ul>
  </section>

</main>
</body>
</html>
```